Tri-fold flyer for Managed Services IT company

We need a tri-fold flyer design for our Managed Services IT company. Our website is here: https://pelicanfjordit.net. While we don't have to match our website we do want to incorporate the logo in the flyer. We would like a flyer that is *very* easy and quick to read/skim over and convey our message. Something like these:

https://www.artkestrel.com/design/58203917

https://47sketchyard.com/postcard-flyer-design/contests/create-lead-generating-flyer-postcard-managed-services-company-815243

http://www.marbleoaksystems.com/managed-services-no-cost-one-month/

Target Market(s)

Business to business IT services

Industry/Entity Type

It Service

Font styles to use
Serif
Sans Serif

Requirements
Must have
• *very* easy and quick to read/skim over and convey our message
Should not have
• verbose, lots of text

```html
<!DOCTYPE html>
<html lang="en">
<head>
<meta charset="utf-8">
<title>Pelican Fjord IT – Tri-fold Flyer</title>
<link href="https://fonts.googleapis.com/css2?family=Open+Sans:wght@400;600;700;800&display=swap" rel="stylesheet">
<style>
  :root{
    --blue-deep:#1a4f9e;
    --blue-mid:#2e6cc0;
    --navy:#2a3378;
    --orange:#e8731f;
    --paper:#ffffff;
    --ink:#1c1c1c;
    --muted:#555b66;
    --backdrop:#8cc4e6;
    --photo-dark:#3a3f48;
    --photo-mid:#7b828d;
  }
  *{box-sizing:border-box;margin:0;padding:0}
  html,body{width:1200px;height:900px;overflow:hidden}
  body{background:var(--backdrop);font-family:"Open Sans",Arial,sans-serif;color:var(--ink);display:flex;align-items:center;justify-content:center}
  .flyer{width:1080px;height:835px;display:flex;box-shadow:0 10px 30px rgba(0,40,80,.25)}
  .panel{width:360px;height:100%;position:relative}
  .panel + .panel{border-left:1px solid #e4e6ea}

  /* inside panel */
  .panel--about{background:linear-gradient(160deg,var(--blue-mid),var(--blue-deep));color:#fff;padding:70px 40px 0 40px}
  .about__title{color:var(--orange);font-weight:700;font-size:30px;line-height:1.1;margin-bottom:18px}
  .about__text{font-size:14px;line-height:1.55;text-align:justify;margin-bottom:22px}
  .about__quote{color:var(--orange);font-weight:700;font-size:27px;line-height:1.15;margin:30px 0 24px}

  /* contact panel */
  .panel--contact{background:var(--paper);padding:50px 36px 0}
  .photo{display:block}
  .photo--team{height:170px;border:3px solid var(--orange);background:linear-gradient(135deg,#e9ecef,#c9cfd6 55%,#9aa3ad)}
  .contact__prompt{text-align:center;color:var(--navy);font-weight:700;font-size:12.5px;line-height:1.45;margin-top:26px}
  .contact__cta{text-align:center;font-weight:700;font-size:17px;color:var(--ink)}
  .photo--contact{height:140px;margin-top:20px;background:linear-gradient(120deg,#f1f2f4,#c8ccd2 60%,#8e6f55);display:flex;align-items:center;padding-left:18px}
  .photo--contact span{font-weight:800;font-size:30px;color:var(--navy)}
  .contact__lines{margin-top:40px;font-size:16px;line-height:1.7;text-align:center}
  .contact__phones{font-size:13px}
  .contact__lines b{font-weight:700}
  .contact__company{font-weight:800;font-size:20px;margin-top:26px;text-align:center}
  .contact__address{text-align:center;font-size:13px;line-height:1.5}

  /* cover panel */
  .panel--cover{background:var(--paper)}
  .brand{height:175px;display:flex;align-items:center;justify-content:center;gap:12px}
  .brand__dot{width:14px;height:14px;border-radius:50%;background:var(--orange)}
  .brand__name{font-weight:600;font-size:30px;letter-spacing:4px;color:var(--navy)}
  .cover__band{height:18px;background:var(--orange)}
  .photo--cover{height:370px;position:relative;background:linear-gradient(150deg,var(--photo-mid),var(--photo-dark) 55%,#22262c)}
  .photo--cover svg{position:absolute;inset:0}
  .cover__welcome{padding:62px 30px 0;font-size:17px;letter-spacing:.5px}
  .cover__tag{padding:4px 30px 0;font-weight:800;font-size:23px;letter-spacing:1.5px;color:var(--orange)}
</style>
</head>
<body>
<main class="flyer">
  <section class="panel panel--about">
    <h2 class="about__title">The DC Metro IT<br>Support Experts</h2>
    <p class="about__text">Pelican Fjord IT has been serving the Bethesda area since 2005, providing IT Support such as technical helpdesk support, computer support, and consulting to small and medium-sized businesses. It's always been our goal to provide enterprise-level IT practices and solutions to the small business sector, with small business prices.</p>
    <p class="about__text">We partner with many types of businesses in the area, and strive to eliminate IT issues before they cause expensive downtime, so you can continue to drive your business forward. Our dedicated staff loves seeing our clients succeed.</p>
    <p class="about__quote">Your success is our success, and as you grow, we grow.</p>
    <p class="about__text">Give those hours wasted on IT problems back to your employees and create a lasting impression on your clients through superior technology services and customer care.</p>
  </section>

  <section class="panel panel--contact">
    <div class="photo photo--team" role="img" aria-label="Photo of a business team meeting around a table"></div>
    <p class="contact__prompt">Interested in seeing what We can do for<br>your Business?</p>
    <p class="contact__cta">Contact Us <span class="contact__prompt" style="font-size:12.5px">to see how We can help you!</span></p>
    <div class="photo photo--contact" role="img" aria-label="Photo of a hand holding a pen over a Contact Us note"><span>Contact Us</span></div>
    <div class="contact__lines">
      <p class="contact__phones">Tel: 301-555-0142 &nbsp;Fax: 000 555 019</p>
      <p><b>E mail:</b> info@pelicanfjordit.net</p>
      <p>www.pelicanfjordit.net</p>
    </div>
    <p class="contact__company">Pelican Fjord IT</p>
    <p class="contact__address">4180 Harbor Mill Road 3A<br>Bethesda, Maryland 20816</p>
  </section>

  <section class="panel panel--cover">
    <div class="brand"><span class="brand__dot"></span><span class="brand__name">PELICAN FJORD</span></div>
    <div class="cover__band"></div>
    <div class="photo photo--cover" role="img" aria-label="Photo of a businessman in a suit using a tablet">
      <svg width="360" height="370" viewBox="0 0 360 370" aria-hidden="true">
        <g stroke="#fff" stroke-width="4">
          <line x1="120" y1="0" x2="120" y2="370"/>
          <line x1="240" y1="0" x2="240" y2="370"/>
          <line x1="0" y1="123" x2="360" y2="123"/>
          <line x1="0" y1="246" x2="360" y2="246"/>
        </g>
      </svg>
    </div>
    <div class="cover__band"></div>
    <p class="cover__welcome">WELCOME TO PELICAN FJORD IT</p>
    <p class="cover__tag">THE DC METRO EXPERTS</p>
  </section>
</main>
</body>
</html>
```